Redesign start page for existing online shop

We are selling building material (chimneys and flue pipes) as well as fireplaces (stoves). For this online shop we need a new start page. The domain is brunnfeld-bauwaren.de. Here you can see the current design. We want a smoother design with just one banner in the middle instead of the three in the first row. The look has to be more professional and trustworthy. You can therefore play with the colors. We want to try some different orange instead of our yellow / orange color. A few more things: - The phone number has to be bigger and more highlighted - So the 5 advantages at the top should be shown in a different way - New design for the products below - New footer

Target Market(s)

Germany and other countries in Europe.

Industry/Entity Type

Home Builder

Number of Pages Required

1 page

Other font styles liked:
• Please se the font on our current site.

Colors
f78f20
f68d4c

Requirements
Must have
• - Clear design - Trustworthy look - All elements Which are now shown shoulderstand be still there after redesigning -
Nice to have
• - See the Following sites to have a clou about our wishes: kalvesto.de flinkrabe.de

```html
<!DOCTYPE html>
<html lang="en">
<head>
<meta charset="utf-8">
<title>Brunnfeld Bauwaren – Chimneys, Flue Pipes and Stoves</title>
<link rel="stylesheet" href="https://fonts.googleapis.com/css2?family=Open+Sans:wght@400;600;700;800&display=swap">
<style>
:root{
  --orange:#f78f20;
  --orange-soft:#f68d4c;
  --dark:#3a3a3a;
  --darker:#2b2b2b;
  --text:#555;
  --muted:#8a8a8a;
  --line:#e3e3e3;
  --light:#f2f2f2;
  --white:#fff;
  --placeholder:#ececec;
}
*{box-sizing:border-box;margin:0;padding:0}
html,body{width:1200px;height:3666px;overflow:hidden;background:var(--white);font-family:"Open Sans",Arial,sans-serif;color:var(--text)}
.wrap{width:1004px;margin:0 auto;position:relative}
a{color:inherit;text-decoration:none}
section,header,footer,nav,.topbar,.bottom{overflow:hidden}

/* top bar */
.topbar{height:36px;border-bottom:1px solid var(--line);font-size:10px;color:var(--muted)}
.topbar .wrap{display:flex;justify-content:space-between;height:100%;align-items:center}
.usp{display:flex;gap:30px}
.usp span::before{content:"";display:inline-block;width:7px;height:7px;border-radius:50%;background:var(--orange);margin-right:7px}
.toplinks{display:flex;height:36px}
.toplinks a{padding:0 18px;display:flex;align-items:center;text-transform:uppercase}
.toplinks a.jobs{background:var(--orange);color:var(--white);padding:0 30px}

/* header */
.header{height:120px}
.header .wrap{display:flex;align-items:center;justify-content:space-between;height:100%}
.logo{display:flex;align-items:center;gap:10px;font-weight:700;color:#4a4a4a;font-size:20px;line-height:1.05;text-transform:uppercase}
.logo i{width:40px;height:40px;border-radius:50%;background:var(--orange)}
.rating{display:flex;align-items:center;gap:10px;border:1px solid var(--line);border-radius:4px;padding:8px 16px;margin-left:120px}
.rating i{width:36px;height:36px;border-radius:50%;background:var(--dark)}
.rating b{font-size:12px;color:#333;display:block}
.rating small{font-size:11px;color:var(--muted)}
.rating em{font-style:normal;color:var(--orange);font-size:13px;letter-spacing:2px}
.hotline .num{display:flex;align-items:center;gap:8px;color:var(--orange);font-size:30px;font-weight:700}
.hotline .hours{font-size:10px;color:var(--muted);margin-top:2px}

/* nav */
.nav{height:56px;background:linear-gradient(#f7f7f7,#e6e6e6);border-top:1px solid var(--line);border-bottom:1px solid #d6d6d6}
.nav ul{list-style:none;display:flex;height:100%;justify-content:space-between;width:1004px;margin:0 auto}
.nav li{display:flex;align-items:center;padding:0 30px;font-size:12px;font-weight:600;color:#444;text-transform:uppercase}
.nav li.active{background:var(--orange);color:var(--white)}

/* hero */
.hero{height:525px;position:relative;background:linear-gradient(180deg,#7fa5c9 0%,#a9c2d8 35%,#c9a37a 55%,#b36d4a 80%,#8e5338 100%)}
.hero-caption{position:absolute;left:670px;top:300px;color:var(--white)}
.hero-caption h3{font-size:16px;font-weight:700}
.hero-caption h1{font-size:44px;font-weight:800;line-height:1.05;letter-spacing:.5px}
.hero-caption p{font-size:14px;width:440px;margin-top:6px;line-height:1.45}
.dots{position:absolute;left:668px;bottom:22px;display:flex;gap:10px}
.dots i{width:13px;height:13px;border-radius:50%;border:2px solid var(--white)}
.dots i.on{background:var(--orange);border-color:var(--orange)}

/* brands */
.brands{height:93px;background:var(--light);border-bottom:1px solid var(--line)}
.brands .wrap{display:flex;justify-content:space-between;align-items:center;height:100%;padding:0 40px}
.brands span{font-size:26px;font-weight:700;color:#a9a9a9}

/* intro + features */
.advantages{height:447px}
.intro{text-align:center;font-size:13px;color:var(--muted);line-height:1.7;width:820px;margin:26px auto 26px}
.features{display:grid;grid-template-columns:repeat(4,1fr);gap:32px}
.feature{border:1px solid var(--line);border-bottom:3px solid var(--orange);height:310px;text-align:center;padding:30px 22px;box-shadow:0 2px 4px rgba(0,0,0,.06)}
.feature svg{width:56px;height:56px}
.feature h4{font-size:12.5px;font-weight:700;color:#333;text-transform:uppercase;margin:30px 0 14px;line-height:1.5}
.feature p{font-size:11px;color:var(--muted);line-height:1.6}
.more{display:inline-block;margin-top:10px;font-size:10.5px;font-weight:700;color:var(--orange);text-decoration:underline;text-transform:uppercase}

/* how it works */
.how{height:477px;background:var(--light);padding-top:38px}
.how h2,.products h2{text-align:center;font-size:26px;font-weight:800;color:#333}
.how .sub{text-align:center;font-size:13px;color:var(--muted);margin-top:4px}
.steps{display:flex;justify-content:space-between;margin-top:26px}
.step{width:200px;text-align:center}
.step .circle{width:118px;height:118px;border-radius:50%;background:var(--dark);margin:0 auto;display:flex;align-items:center;justify-content:center;border:5px solid #dcdcdc}
.step.first .circle{background:var(--orange);border-color:#fbd3a6}
.step h5{font-size:12px;font-weight:700;color:#333;text-transform:uppercase;margin-top:16px;line-height:1.6}
.step.first h5{color:var(--orange)}
.arrow{width:96px;height:40px;margin-top:40px}
.request{margin-top:20px;border:2px solid var(--orange);background:var(--white);height:92px;display:flex;align-items:center;padding:0 26px;gap:24px}
.request h3{font-size:18px;font-weight:700;color:var(--orange);text-transform:uppercase;white-space:nowrap}
.request p{font-size:11px;color:var(--muted);width:340px;line-height:1.6;border-left:1px solid var(--line);padding-left:18px}
.btn{background:var(--orange);color:var(--white);font-size:12px;font-weight:700;padding:12px 22px;border-radius:2px;text-transform:uppercase}
.request .btn{margin-left:auto;white-space:nowrap}

/* products */
.products{height:630px;background:var(--orange);padding-top:44px}
.products h2{color:var(--white)}
.slider-nav{position:absolute;right:0;top:-30px;color:var(--white);font-size:16px;font-weight:700;letter-spacing:6px}
.product-grid{display:grid;grid-template-columns:repeat(4,1fr);gap:40px;margin-top:26px}
.product .card{background:var(--white);height:335px;padding:16px;text-align:center}
.product .pic{height:255px;background:var(--placeholder)}
.product .price{color:var(--orange);font-weight:700;font-size:13px;margin-top:24px}
.product h4{color:var(--white);font-size:13px;font-weight:700;text-align:center;text-transform:uppercase;margin-top:14px}
.product p{color:var(--white);font-size:11px;text-align:center;line-height:1.55;margin-top:6px;padding:0 10px;height:51px;overflow:hidden}
.product .btn{display:block;width:120px;margin:14px auto 0;background:var(--dark);text-align:center;padding:10px 0}

/* seo text */
.seo{height:924px;background:var(--dark);padding-top:44px;color:#d0d0d0;font-size:11px;line-height:1.8}
.seo h2{color:var(--orange);font-size:13px;font-weight:700;text-transform:uppercase;margin-bottom:12px}
.seo h3{color:var(--white);font-size:11.5px;font-weight:700;text-transform:uppercase;margin:22px 0 8px}
.seo p{margin-bottom:10px}
.seo a{color:var(--orange)}

/* footer */
.footer{height:309px;padding-top:40px}
.footer .wrap{display:grid;grid-template-columns:1fr 1fr 1fr;gap:60px}
.footer h4{font-size:13px;font-weight:700;color:var(--orange);text-transform:uppercase;padding-bottom:10px;border-bottom:1px solid var(--line);margin-bottom:18px}
.trust{display:flex;gap:14px;margin-bottom:16px;font-size:11px;line-height:1.55;color:var(--muted)}
.trust i{flex:0 0 130px;height:72px;background:var(--placeholder);border:1px solid var(--line)}
.trust a{color:var(--orange)}
.pay p{font-size:11px;color:var(--muted);line-height:1.6;margin-bottom:16px}
.cards{display:flex;flex-wrap:wrap;gap:8px}
.cards span{width:60px;height:32px;border:1px solid var(--line);font-size:10px;font-weight:700;color:#555;display:flex;align-items:center;justify-content:center}
.contact li{list-style:none;display:flex;gap:12px;font-size:11px;color:var(--muted);line-height:1.6;margin-bottom:16px}
.contact svg{flex:0 0 16px;height:16px}

/* bottom */
.bottom{height:49px;background:var(--light);border-top:1px solid var(--line);font-size:10px;color:var(--muted);text-transform:uppercase}
.bottom .wrap{display:flex;justify-content:space-between;align-items:center;height:100%}
.social{display:flex;align-items:center;gap:8px}
.social i{width:26px;height:26px;border-radius:50%;background:#7a7a7a}
.social i:nth-child(2){background:#4a6ea8}.social i:nth-child(3){background:#3fa9e0}.social i:nth-child(4){background:#1f7fbf}.social i:nth-child(5){background:#c0392b}.social i:nth-child(6){background:#d04a3a}
</style>
</head>
<body>

<div class="topbar"><div class="wrap">
  <div class="usp"><span>In 5 min to the property is offered</span><span>Drive and brands</span><span>Get us requirement</span></div>
  <div class="toplinks"><a class="jobs" href="#">Jobs</a><a href="#">Contact</a><a href="#">Blog</a></div>
</div></div>

<header class="header"><div class="wrap">
  <div class="logo"><i></i><span>Brunnfeld<br>Bauwaren</span></div>
  <div class="rating"><i></i><div><b>SEHR GUT <small>4.79/5.00</small></b><em>★★★★★</em></div></div>
  <div class="hotline">
    <div class="num"><svg width="22" height="22" viewBox="0 0 24 24"><path fill="#f78f20" d="M6.6 10.8a15 15 0 006.6 6.6l2.2-2.2a1 1 0 011-.25 11.4 11.4 0 003.6.57 1 1 0 011 1V20a1 1 0 01-1 1A17 17 0 013 4a1 1 0 011-1h3.5a1 1 0 011 1c0 1.25.2 2.45.57 3.57a1 1 0 01-.25 1z"/></svg>0800 5 318 420</div>
    <div class="hours">MON-FRI | 8:00-20:00 &nbsp;|&nbsp; SAT | 11-17 HRS</div>
  </div>
</div></header>

<nav class="nav"><ul>
  <li class="active">Home</li><li>Online Shop</li><li>Service</li><li>Locations</li><li>Fur Handler</li><li>Installers</li><li>Zen</li><li>Counselor</li>
</ul></nav>

<section class="hero" role="img" aria-label="Two craftsmen fitting a steel chimney on a timber roof under a blue sky">
  <div class="hero-caption">
    <h3>WITH 25 YEARS WARRANTY</h3>
    <h1>CHIMNEY INSATLLERS</h1>
    <p>Sed ut perspiciatis unde omnis iste natus error sit voluptatem accusantium doloremque laudantium, totam...</p>
  </div>
  <div class="dots"><i class="on"></i><i></i><i></i></div>
</section>

<section class="brands"><div class="wrap">
  <span>STOKER</span><span>Varnel</span><span>KELDOR</span><span>Ostrina</span><span>tanvik</span><span>HOLMER</span>
</div></section>

<section class="advantages">
<p class="intro">Sed ut perspiciatis unde omnis iste natus error sit voluptatem accusantium doloremque laudantium, totam rem aperiam, eaque ipsa quae ab illo inventore veritatis et quasi architecto</p>
<div class="wrap features">
  <div class="feature">
    <svg viewBox="0 0 56 56"><rect x="12" y="8" width="28" height="38" rx="2" fill="none" stroke="#f78f20" stroke-width="3"/><path d="M18 20h16M18 27h16M18 34h10" stroke="#f78f20" stroke-width="3"/><circle cx="40" cy="40" r="9" fill="#f78f20"/><path d="M40 35v5h4" stroke="#fff" stroke-width="2" fill="none"/></svg>
    <h4>Mandatory heating offer immediately</h4>
    <p>Sed ut perspiciatis omnisaccusantium doloremque laudantium, totam rem ipsaaspernatur aut odit...</p>
    <a class="more" href="#">Read more info!</a>
  </div>
  <div class="feature">
    <svg viewBox="0 0 56 56"><path d="M12 44L36 20M20 12l24 24" stroke="#f78f20" stroke-width="6" stroke-linecap="round"/><circle cx="40" cy="14" r="7" fill="none" stroke="#f78f20" stroke-width="4"/><rect x="8" y="8" width="10" height="10" fill="#f78f20"/></svg>
    <h4>Over 30 years of quality champions</h4>
    <p>Sed ut perspiciatis omnisaccusantium doloremque laudantium, totam rem ipsaaspernatur aut odit...</p>
    <a class="more" href="#">Read more info!</a>
  </div>
  <div class="feature">
    <svg viewBox="0 0 56 56"><path d="M28 6c6 8-4 12 2 20 3-4 6-5 6-10 4 5 4 12-8 14-10-2-10-12 0-24z" fill="#f78f20"/><path d="M8 32h40a20 16 0 01-40 0z" fill="#f78f20"/></svg>
    <h4>New heating starting at 39 € a month</h4>
    <p>Sed ut perspiciatis omnisaccusantium doloremque laudantium, totam rem ipsaaspernatur aut odit...</p>
    <a class="more" href="#">Read more info!</a>
  </div>
  <div class="feature">
    <svg viewBox="0 0 56 56"><path d="M28 6l18 7v13c0 12-8 20-18 24C18 46 10 38 10 26V13z" fill="#f78f20"/><path d="M20 28l6 6 11-12" stroke="#fff" stroke-width="4" fill="none"/></svg>
    <h4>10 year warranty on their new heating</h4>
    <p>Sed ut perspiciatis omnisaccusantium doloremque laudantium, totam rem ipsaaspernatur aut odit...</p>
    <a class="more" href="#">Read more info!</a>
  </div>
</div>
</section>

<section class="how"><div class="wrap">
  <h2>HOW IT WORKS</h2>
  <p class="sub">In a few steps to the right property is offered for their sanierug</p>
  <div class="steps">
    <div class="step first"><div class="circle"><svg width="48" height="40" viewBox="0 0 48 40"><rect x="8" y="4" width="32" height="22" rx="2" fill="none" stroke="#fff" stroke-width="4"/><path d="M2 32h44" stroke="#fff" stroke-width="5"/></svg></div><h5>Enter data online</h5></div>
    <svg class="arrow" viewBox="0 0 96 40"><path d="M4 32Q48 0 84 22" fill="none" stroke="#c8c8c8" stroke-width="6"/><path d="M80 10l10 16-18 2z" fill="#c8c8c8"/></svg>
    <div class="step"><div class="circle"><svg width="44" height="40" viewBox="0 0 44 40"><path d="M22 2L2 20h6v18h10V26h8v12h10V20h6z" fill="#fff"/></svg></div><h5>Machining allowance and counseling by cros</h5></div>
    <svg class="arrow" viewBox="0 0 96 40"><path d="M4 32Q48 0 84 22" fill="none" stroke="#c8c8c8" stroke-width="6"/><path d="M80 10l10 16-18 2z" fill="#c8c8c8"/></svg>
    <div class="step"><div class="circle"><svg width="34" height="42" viewBox="0 0 34 42"><path d="M2 2h20l10 10v28H2z" fill="#fff"/><path d="M8 20h18M8 27h18M8 34h12" stroke="#3a3a3a" stroke-width="3"/></svg></div><h5>Craftsmen offered also by 2 energy hero</h5></div>
    <svg class="arrow" viewBox="0 0 96 40"><path d="M4 32Q48 0 84 22" fill="none" stroke="#c8c8c8" stroke-width="6"/><path d="M80 10l10 16-18 2z" fill="#c8c8c8"/></svg>
    <div class="step"><div class="circle"><svg width="42" height="42" viewBox="0 0 42 42"><path d="M6 36L24 18" stroke="#fff" stroke-width="7" stroke-linecap="round"/><circle cx="29" cy="13" r="10" fill="#fff"/><circle cx="33" cy="9" r="4" fill="#3a3a3a"/></svg></div><h5>Execution</h5></div>
  </div>
  <div class="request">
    <h3>Now make a non-binding request:</h3>
    <p>Accusantium doloremque laudantium, totam rem aperiam, eaque ipsa quae ab illo inventore veritatis et quasi architecto beatae vitae dicta</p>
    <a class="btn" href="#">Make request ›</a>
  </div>
</div></section>

<section class="products"><div class="wrap">
  <h2>OUR PRODUCTS</h2>
  <div style="position:relative"><span class="slider-nav">‹ ›</span></div>
  <div class="product-grid">
    <div class="product"><div class="card"><div class="pic" role="img" aria-label="Product photo: stainless steel chimney extension"></div><div class="price">FROM € 63,00</div></div>
      <h4>Chimney Extension</h4><p>Fireplace extension configurable produced made to measure and crafted to the highest standard.</p><a class="btn" href="#">Watch now</a></div>
    <div class="product"><div class="card"><div class="pic" role="img" aria-label="Product photo: stainless steel chimney cover"></div><div class="price">FROM € 63,00</div></div>
      <h4>Chimney Cover</h4><p>Fireplace covers for all chimneys purchased individually. Highest durability and quality for your chimney.</p><a class="btn" href="#">Watch now</a></div>
    <div class="product"><div class="card"><div class="pic" role="img" aria-label="Product photo: chimney fan"></div><div class="price">FROM € 63,00</div></div>
      <h4>Chimney Fans</h4><p>Chimney fans for the perfect train in the chimney. Made in Germany for high performance with guaranteed lowest price.</p><a class="btn" href="#">Watch now</a></div>
    <div class="product"><div class="card"><div class="pic" role="img" aria-label="Product photo: black stove pipe"></div><div class="price">FROM € 62,00</div></div>
      <h4>Stovepipe</h4><p>order stovepipe in black or gray cast in premium quality right here. Highest quality for your safety</p><a class="btn" href="#">Watch now</a></div>
  </div>
</div></section>

<section class="seo"><div class="wrap">
  <h2>Stainless steel chimneys, chimney extensions, stovepipes and chimney accessories - at brunnfeld-bauwaren.de buy anything cheap.</h2>
  <p>Can I use a steel chimney for sale on the Internet? This question you have probably never asked. For other products which is a matter of course, but with a stainless steel chimney you do not think first to the online shopping. There are the all-around the subject for several years various platforms steel chimney offer. However, these providers operate their web shop only incidentally. This is reflected in the poor usability and the partly very outdated technology of pages. Brunnfeld Bauwaren has gone a new way here. The goal was a pet shop for stainless steel chimneys and chimney accessories to put on their feet, which is composed not only professionally and according to the latest state of the art, but also gives you the security and usability that you are used to large online platforms in other sectors. With an efficient organization, modern technology and years of experience with the product steel chimney, this claim could be met. Best usability, certified privacy, quality products and expert advice by telephone round your shopping experience from brunnfeld-bauwaren.de.</p>
  <h3>Steel chimney, chimney kit and stainless steel chimney - all from one source.</h3>
  <p>Whether you have a double-walled stainless steel chimney, a chimney restoration looking for your old brick fireplace or chimney kit for your home: here you will find it. In brunnfeld-bauwaren.de you can find a wide range of manufactured in Germany stainless steel chimneys manufacturer Torvalt. These chimneys are manufactured according to the latest production methods of high-quality V4A stainless steel and are subject to stringent quality specifications. The Torvalt GmbH grants you beyond a guarantee of 25 years on each in this online shop acquired steel chimney. Quite simply: security at the best price!</p>
  <p>And another tip: All chimneys can be wonderfully with a stovepipe connect Torvalt. Here there is a large selection at various lengths, colors and angles. In addition, more recently, insulated stovepipes are available. This double-walled furnace tubes reduce the distance that must be maintained to combustible materials to a minimum.</p>
  <h3>Build chimney extension and cowl extension low self.</h3>
  <p>Due to new regulations, the height of many existing chimneys is no longer enough. By structural changes in the environment or many other reasons, it may happen that a chimney extension is necessary. In this online store you will find chimney extensions in versions double or single wall. Each chimney extension is made by hand and can be configured exactly to measure. Here you buy a <a href="#">chimney extension</a> for eternity.</p>
  <h3>Chimney cap, chimney cover and kaminabdeckplatte stainless steel to measure.</h3>
  <p>Older chimney heads are subject to heavy loads due to weather conditions. After many years of rain, sunshine, the cold and the heat chimney tops are porous and begin to crumble. Then it is high time for a kaminabdeckplatte and a <a href="#">chimney cover</a>. In fireplace covers, there are the well-known flat and hood designs. These models have proven themselves over many years and are also mounted on most buildings. In brunnfeld-bauwaren.de we measure chimney covers made of stainless steel or copper with 25 years warranty.</p>
  <h3>Chimney fans, draft stabilizer, fire doors and other specialty products</h3>
  <p>Round this online shop you will also find many other products around the topic of chimney and exhaust technology. Here for example, would the <a href="#">chimney fan</a> to call. A very important device, which allows you to increase the chimney draft electrically. Also from the category of tension control and draft regulation is the draft regulator. These so-called secondary air devices regulate purely mechanical chimney draft. In some cases, may also include a flue gas damper are necessary. In addition to the thermal exhaust flap can be found here also motorized flue dampers, which may be necessary for cascade or chimneys with double occupancy. Is finally even the fireplace door to mention. This component have most of them installed in the chimney side. First suitable replacement, it should be ever noted.</p>
  <p><a href="#">Enjoy shopping, wishes you the team of brunnfeld-bauwaren</a></p>
</div></section>

<footer class="footer"><div class="wrap">
  <div>
    <h4>Shopping safely</h4>
    <div class="trust"><i></i><p>We offer exclusive products of German brand manufacturers. Our full range is manufactured from industry...<br><a href="#">Read More»</a></p></div>
    <div class="trust"><i></i><p>To meet our premium quality and our service pledges, please contact us, of course 25-year...<br><a href="#">Read More»</a></p></div>
  </div>
  <div class="pay">
    <h4>Payment methods</h4>
    <p>Nemo enim ipsam voluptatem quia voluptas sit aspernatur aut odit aut fugit, sed consequuntur magni dolores eos qui ratione...</p>
    <div class="cards"><span>Payora</span><span>Finvo</span><span>Cardix</span><span>Meridan</span><span>Klarweg</span><span>Postlo</span><span>Cardix</span><span>Meridan</span></div>
  </div>
  <div class="contact">
    <h4>Contact info</h4>
    <ul>
      <li><svg viewBox="0 0 16 16"><path d="M8 1a5 5 0 00-5 5c0 4 5 9 5 9s5-5 5-9a5 5 0 00-5-5zm0 7a2 2 0 110-4 2 2 0 010 4z" fill="#f78f20"/></svg><span>Lindenweg 7<br>80331 Munich<br>Germany</span></li>
      <li><svg viewBox="0 0 16 16"><path d="M4.4 7.2a10 10 0 004.4 4.4l1.5-1.5a.7.7 0 01.7-.2 7.6 7.6 0 002.4.4.7.7 0 01.6.7v2.3a.7.7 0 01-.7.7A11.3 11.3 0 012 2.7.7.7 0 012.7 2H5a.7.7 0 01.7.7c0 .8.1 1.6.4 2.4a.7.7 0 01-.2.7z" fill="#f78f20"/></svg><span>Free Consultation : 0800 5 318 420</span></li>
      <li><svg viewBox="0 0 16 16"><rect x="1" y="3" width="14" height="10" rx="1" fill="#f78f20"/><path d="M1 4l7 5 7-5" stroke="#fff" fill="none"/></svg><span>info@brunnfeld-bauwaren.de</span></li>
    </ul>
  </div>
</div></footer>

<div class="bottom"><div class="wrap">
  <span>©brunnfeld-bauwaren 2016 | All rights reserved</span>
  <div class="social"><span>Connect with us</span><i></i><i></i><i></i><i></i><i></i><i></i></div>
</div></div>

</body>
</html>
```